Pagina Lartécnica

The Lartécnica is a company dealing with leasing and selling real estate. The current site can be accessed at www.lartecnica-exemplo.com.br. We intend to redesign the look of the site and for that we would like to redesign the home page and the page with information and pictures of the property. The homepage should maintain the characteristics of the current common design simple, short and straightforward. The page with the data of the properties should be accessed with two changes page as it is currently running. The search from the map by region and should be maintained.
The page containing the information of the property will provide a total of 15 small pictures that when clicked will appear in larger size. The colors to be used should be orange, blue, black and white. The map can be maintained in the current colors.
Updates

Project Deadline Extended
Reason: Payment guarante!!

Payment guaranteed. Deadline for submission of designs April 27.

Industry/Entity Type

Real Estate

Requirements
Must have
• Search by map regions and search box
address
keep colors from the current page
phones
clean look
Nice to have
• clean look
Should not have
• We like the current page. We just want to make it compatible with modern and new design trends and monitors.

```html
<!DOCTYPE html>
<html lang="pt-BR">
<head>
<meta charset="utf-8">
<title>Lartécnica – Imóveis</title>
<link rel="stylesheet" href="https://fonts.googleapis.com/css2?family=Open+Sans:wght@400;600;700&display=swap">
<style>
:root{
  --orange:#f58a07;
  --orange-dark:#e07600;
  --orange-light:#ffb02e;
  --navy:#2c4470;
  --navy-dark:#233961;
  --heading-blue:#2b4f86;
  --footer-text:#c9d5ea;
  --footer-muted:#8fa3c6;
  --ink:#222;
  --page-bg:#eceef2;
  --alert-bg:#f3dada;
  --alert-red:#b00000;
  --white:#fff;
  --ribbon:#1f8fd6;
}
*{box-sizing:border-box;margin:0;padding:0}
html,body{width:1200px;height:830px;overflow:hidden}
body{position:relative;font-family:"Open Sans",Arial,sans-serif;color:var(--ink);background:var(--page-bg)}
.abs{position:absolute}
.backdrop{left:0;top:0;width:1200px;height:640px;background:linear-gradient(90deg,#f1f1f0 0%,#eceef0 45%,#e3e8ef 100%)}
.top-links{left:986px;top:7px;font-size:12px;color:#333;word-spacing:2px}
.sidebar{left:140px;top:0;width:238px;height:562px;background:var(--orange)}
.logo-box{left:131px;top:29px;width:257px;height:88px;background:var(--white);display:flex;align-items:center;justify-content:center;gap:8px;box-shadow:0 2px 4px rgba(0,0,0,.15)}
.logo-box .mark{width:14px;height:14px;background:var(--navy)}
.logo-box .name{font-size:26px;font-weight:700;color:var(--navy)}
.main-nav{left:158px;top:173px;list-style:none}
.main-nav li{height:28px;font-size:15px;font-weight:600;color:var(--white);text-shadow:0 1px 1px rgba(0,0,0,.35);display:flex;align-items:center;gap:10px}
.main-nav li::before{content:"";border-left:5px solid var(--white);border-top:3.5px solid transparent;border-bottom:3.5px solid transparent}
.nav-divider{left:140px;top:457px;width:238px;height:2px;background:var(--orange-dark)}
.phones{left:211px;top:495px;font-size:17px;font-weight:700;color:var(--white);line-height:22px;text-shadow:0 1px 1px rgba(0,0,0,.35)}
.phone-icon{left:160px;top:496px}
.sidebar-shadow{left:135px;top:566px;width:250px;height:14px;border-radius:50%;background:radial-gradient(ellipse at center,rgba(0,0,0,.35),rgba(0,0,0,0) 70%)}
.search-panel{left:397px;top:29px;width:665px;height:88px;background:rgba(255,255,255,.88)}
.label-blue{font-size:14px;font-weight:600;color:var(--heading-blue)}
.search-title{left:426px;top:40px}
.select{left:425px;top:67px;width:184px;height:26px;border:1px solid #cfcfcf;border-radius:4px;background:var(--white);font-size:12px;color:#999;padding:4px 9px}
.select::after{content:"";position:absolute;right:9px;top:10px;border-top:5px solid #555;border-left:4px solid transparent;border-right:4px solid transparent}
.check{top:71px;width:15px;height:15px;border:1px solid #c8c8c8;border-radius:3px;background:var(--white)}
.check.on::after{content:"";position:absolute;left:2px;top:2px;width:9px;height:9px;border-radius:2px;background:#3a9ee0}
.check-label{top:71px;font-size:13px;color:#333}
.btn-search{left:904px;top:64px;width:104px;height:31px;border-radius:4px;background:linear-gradient(#ffb52c,#f58a07);display:flex;align-items:center;justify-content:center;gap:6px;color:var(--white);font-size:16px;font-weight:700;text-shadow:0 1px 1px rgba(0,0,0,.25)}
.map-title{left:426px;top:133px}
.rec-title{left:765px;top:133px}
.region-map{left:396px;top:160px;width:355px;height:405px;border:3px solid var(--white);background:linear-gradient(160deg,#c9d8ea 0%,#a9c0de 45%,#d8dcc8 70%,#b9cde6 100%);box-shadow:0 0 2px rgba(0,0,0,.2)}
.listing{left:765px;width:134px;height:88px;border:2px solid var(--white);box-shadow:0 0 2px rgba(0,0,0,.3);overflow:hidden}
.listing .photo{width:100%;height:100%;background:linear-gradient(180deg,#b9d0ea 0%,#d9d4c4 45%,#b3643a 70%,#5b7a45 100%)}
.listing.active{border-color:var(--navy)}
.ribbon{position:absolute;right:-20px;top:8px;width:80px;height:15px;background:var(--ribbon);transform:rotate(40deg);color:var(--white);font-size:9px;font-weight:700;text-align:center;line-height:15px}
.details{left:914px;font-size:13px;line-height:16px}
.details dt{float:left;clear:left;width:48px;font-weight:700}
.details dd{margin-left:48px}
.alert{left:397px;top:575px;width:336px;height:52px;background:var(--alert-bg);border-radius:3px;padding:10px 0 0 60px;font-size:13px;line-height:15px;color:var(--alert-red)}
.alert svg{position:absolute;left:10px;top:12px}
.footer{left:0;top:640px;width:1200px;height:155px;background:var(--navy)}
.footer-bottom{left:0;top:795px;width:1200px;height:35px;background:var(--navy-dark);text-align:center;font-size:12px;color:var(--footer-muted);line-height:40px}
.f-head{top:656px;font-size:14px;font-weight:600;color:var(--footer-muted)}
.f-list{top:682px;list-style:none;font-size:13px;font-weight:600;color:var(--footer-text)}
.f-list li{height:20.7px;display:flex;align-items:center;gap:5px}
.f-list li::before{content:"";border-left:3px solid var(--footer-text);border-top:2.5px solid transparent;border-bottom:2.5px solid transparent}
.f-divider{left:598px;top:656px;width:1px;height:110px;background:#46608f}
.company{left:621px;top:682px;font-size:14px;font-weight:600;color:var(--footer-text)}
.address{left:621px;top:703px;font-size:13px;line-height:20.7px;color:var(--footer-text)}
.contact-table{left:841px;top:682px;font-size:13px;line-height:20.7px;color:var(--footer-text)}
.contact-table dt{float:left;clear:left;width:67px}
.contact-table a{color:var(--footer-text)}
</style>
</head>
<body>
<div class="abs backdrop" role="img" aria-label="Faded road map of the city region as page background"></div>
<div class="abs top-links">Login | Help</div>

<aside>
  <div class="abs sidebar"></div>
  <div class="abs logo-box"><span class="mark"></span><span class="name">Lartécnica</span></div>
  <ul class="abs main-nav">
    <li>A empresa</li><li>Localizacao</li><li>Area Restrita</li><li>Fale Conosco</li>
    <li>Cadastre seu imovel</li><li>Informacoes ao Proprietario</li><li>Informacoes ao Locatario</li><li>Solicite seu imovel</li>
  </ul>
  <div class="abs nav-divider"></div>
  <svg class="abs phone-icon" width="42" height="38" viewBox="0 0 42 38" aria-hidden="true">
    <path d="M2 10 Q21 -2 40 10 L36 15 L30 12 L30 8 Q21 5 12 8 L12 12 L6 15 Z" fill="#fff"/>
    <g fill="#fff"><circle cx="14" cy="20" r="2.5"/><circle cx="21" cy="20" r="2.5"/><circle cx="28" cy="20" r="2.5"/><circle cx="14" cy="27" r="2.5"/><circle cx="21" cy="27" r="2.5"/><circle cx="28" cy="27" r="2.5"/><circle cx="14" cy="34" r="2.5"/><circle cx="21" cy="34" r="2.5"/><circle cx="28" cy="34" r="2.5"/></g>
  </svg>
  <div class="abs phones">(48) 300 12 34<br>(48) 9000 4567</div>
  <div class="abs sidebar-shadow"></div>
</aside>

<section>
  <div class="abs search-panel"></div>
  <div class="abs label-blue search-title">Busca de imoveis</div>
  <div class="abs select">Todos</div>
  <div class="abs check on" style="left:638px"></div>
  <div class="abs check-label" style="left:662px">Para comprar</div>
  <div class="abs check" style="left:769px"></div>
  <div class="abs check-label" style="left:794px">Para alugar</div>
  <div class="abs btn-search">
    <svg width="18" height="18" viewBox="0 0 18 18" aria-hidden="true"><circle cx="7" cy="7" r="5" fill="none" stroke="#fff" stroke-width="2.5"/><path d="M10.5 10.5 L16 16" stroke="#fff" stroke-width="3" stroke-linecap="round"/></svg>
    Buscar
  </div>
</section>

<section>
  <div class="abs label-blue map-title">Buscar imovel po regiao (location)</div>
  <div class="abs region-map" role="img" aria-label="Clickable map of the island and mainland split into regions: Norte, Continente, Centro, Leste and Sul, with Norte highlighted in orange"></div>

  <div class="abs label-blue rec-title">We Recomended</div>

  <div class="abs listing" style="top:163px"><div class="photo" role="img" aria-label="Photo of apartment building with palm trees"></div><span class="ribbon">NEW</span></div>
  <dl class="abs details" style="top:160px"><dt>Bairro:</dt><dd>Coqueiros</dd><dt>Cidade:</dt><dd>CONTINENTE</dd><dt>Valor:</dt><dd>2.060,00</dd><dt>Cond.:</dt><dd>330,00</dd><dt>IPTU:</dt><dd>87,89</dd></dl>

  <div class="abs listing active" style="top:268px"><div class="photo" role="img" aria-label="Photo of apartment building with palm trees"></div></div>
  <dl class="abs details" style="top:266px"><dt>Bairro:</dt><dd>Coqueiros</dd><dt>Cidade:</dt><dd>CONTINENTE</dd><dt>Valor:</dt><dd>2.060,00</dd><dt>Cond.:</dt><dd>330,00</dd><dt>IPTU:</dt><dd>87,89</dd></dl>

  <div class="abs listing" style="top:373px"><div class="photo" role="img" aria-label="Photo of apartment building with palm trees"></div><span class="ribbon">NEW</span></div>
  <dl class="abs details" style="top:371px"><dt>Bairro:</dt><dd>Coqueiros</dd><dt>Cidade:</dt><dd>CONTINENTE</dd><dt>Valor:</dt><dd>2.060,00</dd><dt>Cond.:</dt><dd>330,00</dd><dt>IPTU:</dt><dd>87,89</dd></dl>

  <div class="abs listing" style="top:477px"><div class="photo" role="img" aria-label="Photo of apartment building with palm trees"></div></div>
  <dl class="abs details" style="top:472px"><dt>Bairro:</dt><dd>Coqueiros</dd><dt>Cidade:</dt><dd>CONTINENTE</dd><dt>Valor:</dt><dd>2.060,00</dd><dt>Cond.:</dt><dd>330,00</dd><dt>IPTU:</dt><dd>87,89</dd></dl>

  <div class="abs alert">
    <svg width="30" height="26" viewBox="0 0 30 26" aria-hidden="true"><path d="M15 1 L29 25 L1 25 Z" fill="#f5a81c" stroke="#c57a00" stroke-width="1.5" stroke-linejoin="round"/><rect x="13.6" y="8" width="2.8" height="9" fill="#333"/><rect x="13.6" y="19.5" width="2.8" height="2.8" fill="#333"/></svg>
    <strong>Allert!</strong> Lorem ipsum dolor sit amet, consect etuer adipiscing elit.
  </div>
</section>

<footer>
  <div class="abs footer"></div>
  <div class="abs f-head" style="left:157px">MENU</div>
  <ul class="abs f-list" style="left:157px"><li>A empresa</li><li>Localização</li><li>Área Restrita</li><li>Fale Conosco</li></ul>
  <ul class="abs f-list" style="left:271px"><li>Cadastre seu imóvel</li><li>Informações ao Proprietário</li><li>Informações ao Locatário</li><li>Solicite seu imóvel</li></ul>
  <div class="abs f-head" style="left:465px">CUSTOMERS</div>
  <ul class="abs f-list" style="left:466px"><li>Privacy</li><li>Terms of use</li><li>Contact Support</li><li>FAQ</li></ul>
  <div class="abs f-divider"></div>
  <div class="abs f-head" style="left:619px">CONTACT</div>
  <div class="abs company">Lartécnica</div>
  <div class="abs address">Rua das Acácias, 148<br>Esquina com a Rua Beira-Mar<br>Centro - Florianópolis</div>
  <dl class="abs contact-table"><dt>CEP :</dt><dd>88015-210</dd><dt>Fax :</dt><dd>(48) 3000-1234</dd><dt>Locação :</dt><dd>(48) 3000-5678</dd><dt>Email :</dt><dd><a href="#">info@lartecnica-exemplo.com.br</a></dd></dl>
  <div class="abs footer-bottom">© (C) 2013 - Lartécnica - Todos os direitos reservados.</div>
</footer>
</body>
</html>
```